Telecommunications/Power civil contractor needs business card design

Were a new telecommunications/power underground civil contractor that is looking for a new business card design. Our company colours are silver or grey and orange. Feel free to use the white background logo or the black background logo.

Target Market(s)

Local contractors, utility companies, private sector mining/energy companies, developers.

Industry/Entity Type

Telecommunications

Contact Information for Business Card

Each card will need the following info:
Persons name:
Title:
E-mail:
Phone number:
Shop Address:
Mailing Address:

Requirements
Must have
• Each card will need the following info:
• Persons name:
• Title:
• E-mail:
• Phone number:
• Shop Address:
• Mailing Address:

```html
<!DOCTYPE html>
<html lang="en">
<head>
<meta charset="utf-8">
<title>Tanner Ridge Civil Inc — Business Card</title>
<link rel="stylesheet" href="https://fonts.googleapis.com/css2?family=Montserrat:wght@400;500;600;800&display=swap">
<style>
  :root {
    --page-bg: #e9e6e1;
    --card-black: #0d0d0e;
    --card-black-hi: #2a2a2c;
    --silver-light: #f4f4f4;
    --silver-mid: #d6d6d8;
    --silver-dark: #a9a9ad;
    --band-grey: #8e8f93;
    --orange: #f26a21;
    --white: #ffffff;
    --ink: #1c1c1e;
  }
  * { margin: 0; padding: 0; box-sizing: border-box; }
  html, body { width: 1200px; height: 1022px; overflow: hidden; }
  body {
    background: var(--page-bg);
    font-family: "Montserrat", Arial, sans-serif;
    position: relative;
  }
  .business-card {
    position: absolute;
    left: 100px;
    top: 225px;
    width: 1000px;
    height: 572px;
    border-radius: 26px;
    overflow: hidden;
    box-shadow: 0 18px 40px rgba(0,0,0,0.25);
  }
  .card-shapes { position: absolute; inset: 0; }
  .brand-wordmark {
    position: absolute;
    left: 70px;
    top: 168px;
    color: var(--white);
    font-weight: 800;
    font-size: 44px;
    line-height: 1.05;
    letter-spacing: 1px;
  }
  .person-name {
    position: absolute;
    left: 70px;
    top: 290px;
    color: var(--orange);
    font-weight: 600;
    font-size: 34px;
    letter-spacing: 1px;
  }
  .person-title {
    position: absolute;
    left: 70px;
    top: 336px;
    color: var(--white);
    font-weight: 400;
    font-size: 21px;
  }
  .addresses {
    position: absolute;
    left: 70px;
    top: 388px;
    color: var(--white);
    font-weight: 400;
    font-size: 22px;
    line-height: 1.4;
  }
  .addresses p + p { margin-top: 10px; }
  .logo-lockup {
    position: absolute;
    left: 550px;
    top: 44px;
    display: flex;
    align-items: center;
    gap: 18px;
  }
  .logo-circle {
    width: 170px;
    height: 170px;
    border-radius: 50%;
    background: var(--card-black);
  }
  .logo-name {
    color: var(--ink);
    font-weight: 800;
    font-size: 24px;
    letter-spacing: 1px;
    line-height: 1.15;
  }
  .contact-icons {
    position: absolute;
    right: 40px;
    top: 250px;
    display: flex;
    gap: 14px;
  }
  .contact-icons svg { width: 20px; height: 20px; }
  .contact-list {
    position: absolute;
    right: 40px;
    top: 290px;
    text-align: right;
    color: var(--ink);
    font-weight: 500;
    font-size: 22px;
    line-height: 1.5;
    list-style: none;
  }
</style>
</head>
<body>
  <article class="business-card">
    <svg class="card-shapes" viewBox="0 0 1000 572" width="1000" height="572" aria-hidden="true">
      <defs>
        <linearGradient id="silverFace" x1="0" y1="0" x2="1" y2="1">
          <stop offset="0" stop-color="var(--silver-dark)"/>
          <stop offset="0.35" stop-color="var(--silver-light)"/>
          <stop offset="0.7" stop-color="var(--silver-mid)"/>
          <stop offset="1" stop-color="var(--silver-light)"/>
        </linearGradient>
        <linearGradient id="blackFace" x1="0" y1="0" x2="1" y2="0">
          <stop offset="0" stop-color="var(--card-black)"/>
          <stop offset="0.75" stop-color="var(--card-black-hi)"/>
          <stop offset="1" stop-color="var(--card-black)"/>
        </linearGradient>
      </defs>
      <rect class="silver-face" width="1000" height="572" fill="url(#silverFace)"/>
      <path class="orange-band" d="M0,0 H690 C610,130 575,200 615,310 C650,420 610,520 575,572 H0 Z" fill="var(--orange)"/>
      <path class="grey-band" d="M0,0 H668 C590,125 556,200 596,310 C630,420 590,520 553,572 H0 Z" fill="var(--band-grey)"/>
      <path class="black-face" d="M0,0 H652 C575,125 540,200 580,310 C614,420 574,520 535,572 H0 Z" fill="url(#blackFace)"/>
    </svg>

    <h1 class="brand-wordmark">TANNER RIDGE<br>CIVIL INC</h1>
    <h2 class="person-name">MARLA KEATING</h2>
    <p class="person-title">Director</p>
    <div class="addresses">
      <p class="shop-address">48 Quarry Lane<br>Millbrook, NY 12545</p>
      <p class="mailing-address">PO BOX 3186<br>RIDGEVIEW, CA 91302</p>
    </div>

    <div class="logo-lockup">
      <div class="logo-circle"></div>
      <span class="logo-name">TANNER<br>RIDGE</span>
    </div>

    <div class="contact-icons" aria-hidden="true">
      <svg class="icon-phone" viewBox="0 0 20 20"><path d="M5 2 L8 2 L9 6 L7 8 C8 11 9 12 12 13 L14 11 L18 12 L18 15 C18 17 16 18 14 18 C8 17 3 12 2 6 C2 4 3 2 5 2 Z" fill="var(--orange)"/></svg>
      <svg class="icon-mobile" viewBox="0 0 20 20"><rect x="5" y="1" width="10" height="18" rx="2" fill="none" stroke="var(--orange)" stroke-width="2"/><circle cx="10" cy="15.5" r="1.2" fill="var(--orange)"/></svg>
      <svg class="icon-mail" viewBox="0 0 20 20"><rect x="1.5" y="4" width="17" height="12" rx="1.5" fill="none" stroke="var(--orange)" stroke-width="2"/><path d="M2 5 L10 11 L18 5" fill="none" stroke="var(--orange)" stroke-width="2"/></svg>
      <svg class="icon-web" viewBox="0 0 20 20"><circle cx="10" cy="10" r="8" fill="none" stroke="var(--orange)" stroke-width="2"/><path d="M2 10 H18 M10 2 C6 6 6 14 10 18 M10 2 C14 6 14 14 10 18" fill="none" stroke="var(--orange)" stroke-width="1.5"/></svg>
    </div>

    <ul class="contact-list">
      <li class="phone">+330 5182-4409</li>
      <li class="phone">+330 6371-2284</li>
      <li class="email">info@tannerridgecivil.com</li>
      <li class="website">www.tannerridgecivil.com</li>
    </ul>
  </article>
</body>
</html>
```